TALBRIDGE ELEVATOR CORP

LOOKING FOR BLACK MATTE BACKGROUND WITH GLOSS DESIGN
NEED RAISED UV ON LOGO AND LETTERING , WITH ROUNDED CORNERS AND COLORED EDGES ( FLOURECENT BLUE)

```html
<!DOCTYPE html>
<html lang="en">
<head>
<meta charset="utf-8">
<title>Talbridge Elevator Corp – Business Card</title>
<link href="https://fonts.googleapis.com/css2?family=PT+Sans:wght@400;700&display=swap" rel="stylesheet">
<style>
  :root {
    --backdrop: #e6e6e6;
    --front-base: #050505;
    --front-side: #1c1c1c;
    --back-base: #163063;
    --back-deep: #0f2452;
    --glow: #ffffff;
    --glow-blue: #7fb2ff;
    --text-light: #ffffff;
    --text-muted: #b8b8b8;
  }
  * { margin: 0; padding: 0; box-sizing: border-box; }
  html, body {
    width: 900px; height: 1200px; overflow: hidden;
    background: var(--backdrop);
    font-family: "PT Sans", sans-serif;
  }
  .canvas { position: relative; width: 900px; height: 1200px; }
  .card {
    position: absolute; left: 113px; width: 675px; height: 405px;
    border-radius: 46px; overflow: hidden;
  }
  .card-front { top: 158px; background: var(--front-base); }
  .card-back { top: 637px; background: linear-gradient(160deg, var(--back-base), var(--back-deep)); }
  .card-art { position: absolute; inset: 0; width: 100%; height: 100%; }

  .brand-name {
    position: absolute; left: 0; right: 0; top: 108px;
    text-align: center; color: var(--text-light);
    font-size: 40px; font-weight: 400; letter-spacing: 1px;
  }
  .company-name {
    position: absolute; left: 0; right: 0; top: 260px;
    text-align: center; color: var(--text-light);
    font-size: 38px; font-weight: 400; letter-spacing: -1px;
    text-shadow: 0 0 8px rgba(255,255,255,0.55);
  }
  .company-tagline {
    position: absolute; left: 0; right: 0; top: 313px;
    text-align: center; color: var(--text-muted);
    font-size: 21px; font-weight: 400; letter-spacing: -0.3px;
  }

  .person { position: absolute; left: 0; width: 302px; top: 36px; text-align: right; color: var(--text-light); text-shadow: 0 0 8px rgba(255,255,255,0.5); }
  .person-name { font-size: 38px; line-height: 44px; font-weight: 400; letter-spacing: -1.5px; }
  .person-role { font-size: 22px; line-height: 28px; font-weight: 400; letter-spacing: -0.3px; }

  .contact { position: absolute; left: 45px; top: 213px; color: var(--text-light); font-size: 15px; line-height: 18.5px; letter-spacing: -0.3px; }
  .contact-row { display: flex; align-items: flex-start; }
  .contact-row svg { width: 14px; height: 14px; margin: 2px 8px 0 0; flex: none; }
  .contact-gap { height: 17px; }
</style>
</head>
<body>
<div class="canvas">

  <section class="card card-front">
    <svg class="card-art" viewBox="0 0 675 405" aria-hidden="true">
      <defs>
        <filter id="soft-glow"><feGaussianBlur stdDeviation="2"/></filter>
      </defs>
      <path d="M0 40 C40 160 120 330 241 405 L0 405 Z" fill="var(--front-side)"/>
      <path d="M478 0 C560 90 620 250 627 405 L675 405 L675 0 Z" fill="var(--front-side)"/>
      <g stroke="var(--glow)" fill="none">
        <path d="M4 46 C30 200 120 340 241 405" stroke-width="4" opacity="0.4" filter="url(#soft-glow)"/>
        <path d="M4 46 C30 200 120 340 241 405" stroke-width="1.4"/>
        <path d="M50 18 C70 150 110 250 200 360" stroke-width="1.2" opacity="0.7"/>
        <path d="M478 0 C560 90 620 250 627 405" stroke-width="4" opacity="0.4" filter="url(#soft-glow)"/>
        <path d="M478 0 C560 90 620 250 627 405" stroke-width="1.4"/>
        <path d="M507 4 C590 70 655 200 672 360" stroke-width="1.2" opacity="0.8"/>
      </g>
    </svg>
    <p class="brand-name">TALBRIDGE</p>
    <h1 class="company-name">TALBRIDGE ELEVATOR CORP</h1>
    <p class="company-tagline">- ELEVATOR SERVICES -</p>
  </section>

  <section class="card card-back">
    <svg class="card-art" viewBox="0 0 675 405" aria-hidden="true">
      <defs>
        <filter id="blue-glow"><feGaussianBlur stdDeviation="3"/></filter>
        <radialGradient id="spark"><stop offset="0" stop-color="var(--glow-blue)" stop-opacity="0.9"/><stop offset="1" stop-color="var(--glow-blue)" stop-opacity="0"/></radialGradient>
      </defs>
      <path d="M343 0 C420 60 455 160 463 405 L568 405 C540 250 470 90 355 0 Z" fill="var(--back-deep)" opacity="0.6"/>
      <g fill="none">
        <path d="M343 0 C420 60 455 160 463 405" stroke="var(--glow-blue)" stroke-width="5" opacity="0.6" filter="url(#blue-glow)"/>
        <path d="M343 0 C420 60 455 160 463 405" stroke="var(--glow)" stroke-width="1.5"/>
        <path d="M355 0 C470 90 540 250 568 405" stroke="var(--glow-blue)" stroke-width="5" opacity="0.6" filter="url(#blue-glow)"/>
        <path d="M355 0 C470 90 540 250 568 405" stroke="var(--glow)" stroke-width="1.5"/>
      </g>
      <circle cx="348" cy="5" r="22" fill="url(#spark)"/>
      <circle cx="503" cy="145" r="26" fill="url(#spark)"/>
      <circle cx="460" cy="230" r="22" fill="url(#spark)"/>
      <circle cx="568" cy="395" r="20" fill="url(#spark)"/>
    </svg>

    <div class="person">
      <h2 class="person-name">DANIEL HARLOW</h2>
      <p class="person-role">PRESIDENT</p>
    </div>

    <div class="contact">
      <div class="contact-row">
        <svg viewBox="0 0 14 14"><path d="M7 1 L13 7 L11 7 L11 13 L8.5 13 L8.5 9 L5.5 9 L5.5 13 L3 13 L3 7 L1 7 Z" fill="var(--text-light)"/></svg>
        <span>TALBRIDGE ELEVATOR CORP</span>
      </div>
      <div class="contact-row">
        <svg viewBox="0 0 14 14"><path d="M7 13 C4 9 2.5 7 2.5 5 A4.5 4.5 0 0 1 11.5 5 C11.5 7 10 9 7 13 Z" fill="none" stroke="var(--text-light)" stroke-width="1"/><circle cx="7" cy="5" r="1.6" fill="none" stroke="var(--text-light)" stroke-width="1"/></svg>
        <span>2207 FERRIS PARK AVENUE<br>BRONX, NY 10461</span>
      </div>
      <div class="contact-gap"></div>
      <div class="contact-row">
        <svg viewBox="0 0 14 14"><rect x="1" y="3" width="12" height="8" fill="var(--text-light)"/><path d="M1 3 L7 8 L13 3" fill="none" stroke="var(--back-base)" stroke-width="1"/></svg>
        <span>TALBRIDGEELEVATOR@MAIL.COM</span>
      </div>
      <div class="contact-row">
        <svg viewBox="0 0 14 14"><g fill="none" stroke="var(--text-light)" stroke-width="1"><circle cx="7" cy="7" r="5.5"/><ellipse cx="7" cy="7" rx="2.4" ry="5.5"/><path d="M1.5 7 H12.5 M2.3 4.3 H11.7 M2.3 9.7 H11.7"/></g></svg>
        <span>TALBRIDGEELEVATORNY.COM</span>
      </div>
      <div class="contact-row">
        <svg viewBox="0 0 14 14"><path d="M7 13 C4 9 2.5 7 2.5 5 A4.5 4.5 0 0 1 11.5 5 C11.5 7 10 9 7 13 Z" fill="none" stroke="var(--text-light)" stroke-width="1"/><circle cx="7" cy="5" r="1.6" fill="none" stroke="var(--text-light)" stroke-width="1"/></svg>
        <span>516-555-0147<br>ESTABLISHED 1978</span>
      </div>
    </div>
  </section>

</div>
</body>
</html>
```